Business cards and Stationary for Bright Learning Alliance
A Chinese Education Consulting Company
Business cards and Stationary for Bright Learning Alliance - Education
Creative Brief
Professional
Dennis R. Tolwy
Manager
7214 Marlow Court, San Ramon, CA 94583
dennistolwy@brilearnal.com
www.brilearnal.com
Please leave abundant space for multi address, (2) multi cell phones (3)

```html
<!DOCTYPE html>
<html lang="en">
<head>
<meta charset="utf-8">
<title>Bright Learning Alliance — Business Card</title>
<link rel="stylesheet" href="https://fonts.googleapis.com/css2?family=Open+Sans:wght@400;600;700&display=swap">
<style>
  :root {
    --backdrop: #e9e6e1;
    --card: #fdfdfd;
    --red: #c8141b;
    --red-dark: #8e0a0f;
    --gold: #c9a24a;
    --gold-light: #f1dc9c;
    --ink: #4a4a4a;
    --rule: #d4d4d4;
  }
  * { margin: 0; padding: 0; box-sizing: border-box; }
  html, body { width: 1200px; height: 914px; overflow: hidden; }
  body {
    background: var(--backdrop);
    font-family: "Open Sans", Arial, sans-serif;
    position: relative;
  }
  .business-card {
    position: absolute;
    left: 100px; top: 171px;
    width: 1000px; height: 572px;
    background: var(--card);
    box-shadow: 0 6px 24px rgba(0,0,0,.18);
    overflow: hidden;
  }
  .brand-mark {
    position: absolute;
    left: 120px; top: 236px;
    width: 210px;
    display: flex; align-items: center; gap: 12px;
  }
  .brand-dot {
    flex: none;
    width: 26px; height: 26px;
    border-radius: 50%;
    background: var(--red);
  }
  .brand-name {
    color: var(--red);
    font-weight: 700;
    font-size: 22px;
    line-height: 1.2;
  }
  .divider {
    position: absolute;
    left: 350px; top: 165px;
    width: 1px; height: 245px;
    background: var(--rule);
  }
  .contact {
    position: absolute;
    left: 372px; top: 150px;
    color: var(--ink);
    font-size: 15px;
    line-height: 1.55;
  }
  .contact-name {
    color: var(--red);
    font-weight: 700;
    font-size: 22px;
    line-height: 1.2;
  }
  .contact-title {
    font-size: 15px;
    margin-bottom: 14px;
  }
  .contact-list { list-style: none; }
  .contact-list li {
    display: flex; align-items: center; gap: 8px;
    min-height: 23px;
  }
  .contact-list li.continued { padding-left: 24px; }
  .icon {
    flex: none;
    width: 16px; height: 16px;
  }
  .card-bands {
    position: absolute;
    left: 0; bottom: 0;
    width: 1000px; height: 150px;
  }
</style>
</head>
<body>
  <div class="business-card">
    <div class="brand-mark">
      <span class="brand-dot"></span>
      <span class="brand-name">Bright Learning Alliance</span>
    </div>

    <div class="divider"></div>

    <div class="contact">
      <p class="contact-name">Dennis R. Tolwy</p>
      <p class="contact-title">Manager</p>
      <ul class="contact-list">
        <li>
          <svg class="icon" viewBox="0 0 16 16"><circle cx="8" cy="8" r="8" fill="#c8141b"/><path d="M4 8.5 8 5l4 3.5M5.5 7.5V11h5V7.5" fill="none" stroke="#fff" stroke-width="1.3"/></svg>
          7214 Marlow Court,
        </li>
        <li class="continued">San Ramon, CA 94583</li>
        <li>
          <svg class="icon" viewBox="0 0 16 16"><circle cx="8" cy="8" r="8" fill="#c8141b"/><path d="M5.5 4.5c-.8.6-.8 1.8.3 3.4 1.2 1.8 2.7 3.3 4 3.7.9.3 1.6-.3 1.8-.9l-1.6-1.2-.9.6c-.8-.4-1.6-1.3-2-2.1l.6-.9L6.5 4.4z" fill="#fff"/></svg>
          +1 925-555-014-7
        </li>
        <li>
          <svg class="icon" viewBox="0 0 16 16"><circle cx="8" cy="8" r="8" fill="#c8141b"/><rect x="5.5" y="3.5" width="5" height="9" rx="1" fill="none" stroke="#fff" stroke-width="1.2"/><circle cx="8" cy="11" r=".7" fill="#fff"/></svg>
          +86-139-555-027-61
        </li>
        <li>
          <svg class="icon" viewBox="0 0 16 16"><circle cx="8" cy="8" r="8" fill="#c8141b"/><rect x="4" y="5" width="8" height="6" fill="none" stroke="#fff" stroke-width="1.1"/><path d="M4 5l4 3.3L12 5" fill="none" stroke="#fff" stroke-width="1.1"/></svg>
          dennistolwy@brilearnal.com
        </li>
        <li>
          <svg class="icon" viewBox="0 0 16 16"><circle cx="8" cy="8" r="8" fill="#c8141b"/><circle cx="8" cy="8" r="4" fill="none" stroke="#fff" stroke-width="1.1"/><path d="M4 8h8M8 4c-1.6 2.4-1.6 5.6 0 8M8 4c1.6 2.4 1.6 5.6 0 8" fill="none" stroke="#fff" stroke-width=".9"/></svg>
          www.brilearnal.com
        </li>
      </ul>
    </div>

    <svg class="card-bands" viewBox="0 0 1000 150" preserveAspectRatio="none" aria-hidden="true">
      <defs>
        <linearGradient id="redBand" x1="0" y1="0" x2="0" y2="1">
          <stop offset="0" stop-color="#e3262c"/>
          <stop offset="1" stop-color="#8e0a0f"/>
        </linearGradient>
        <linearGradient id="goldBand" x1="0" y1="0" x2="1" y2="1">
          <stop offset="0" stop-color="#a9802f"/>
          <stop offset=".45" stop-color="#f1dc9c"/>
          <stop offset="1" stop-color="#b88d3a"/>
        </linearGradient>
      </defs>
      <polygon points="0,18 560,18 600,62 0,62" fill="url(#redBand)"/>
      <polygon points="545,75 1000,75 1000,128 590,128" fill="url(#goldBand)"/>
    </svg>
  </div>
</body>
</html>
```